SEAFOOD PACKAGING (Products for consumer)

We are looking to create packaging for various seafood products such as octopus and squid. We plan to sell our products in upscale supermarkets.

We are specializing in cut octopus this time.

Please include our company logo. Also, please leave a transparent area so that customers can see the product inside.
Updates

We want to show what is inside, so a picture of the octopus is not required. We need something simple and sophisticated.

Target Market(s)

upscale store in US and ASIA

Industry/Entity Type

Fisheries dealer

Requirements
Must have
• Please include the attached logo,Blue one is preferred.Please leave a transparent part so that the contents of the product can be seen by the consumer.1. product name on packaging →CUT OCTOPUS,TAKO SASHIMI,Highest quality,Top quality etc... 3. What text information should be on the packaging →(It may be edited, but this is the image) The raw materials are caught in a very clean environment and processed in a modern factory with ZEK certification. We are committed to additive-free products. 4. Packing size(cm/inch)→it will be about 19cm*22cm. 5. what kind of packaging do you use →PP or PA 6. dll →ai,jag
Nice to have
• https://quillmora.example/shots/4829174-Velka-Reef We need something simple and sophisticated like this one.
Should not have
• We want to show what is inside, so a picture of the octopus is not required. We need something simple and sophisticated.

```html
<!DOCTYPE html>
<html lang="en">
<head>
<meta charset="utf-8">
<title>Maren Cut Octopus – Package Front</title>
<link rel="stylesheet" href="https://fonts.googleapis.com/css2?family=Poppins:wght@400;500;600;800&family=Playfair+Display:wght@600&family=Oswald:wght@600&display=swap">
<style>
  :root {
    --stage-light: #1ba8c9;
    --stage-deep: #0a6587;
    --navy: #0a1828;
    --navy-mid: #0e2c44;
    --water-a: #0f4f6d;
    --water-b: #1a7792;
    --product-a: #c9c3c0;
    --product-b: #8c7f7f;
    --gold-light: #f8e394;
    --gold-mid: #e2c66e;
    --gold-deep: #b18c3a;
    --white: #ffffff;
    --ink: #0d1a2b;
  }
  * { margin: 0; padding: 0; box-sizing: border-box; }
  html, body { width: 1200px; height: 1200px; overflow: hidden; }
  body {
    background: linear-gradient(200deg, var(--stage-light) 0%, var(--stage-deep) 100%);
    position: relative;
    font-family: "Poppins", sans-serif;
  }
  .package {
    position: absolute;
    left: 226px; top: 167px;
    width: 748px; height: 866px;
    background: var(--navy);
    box-shadow: 0 12px 40px rgba(0, 20, 40, 0.35);
    overflow: hidden;
  }
  .water-backdrop {
    position: absolute; left: 0; top: 0; width: 100%; height: 400px;
    background:
      radial-gradient(ellipse at 70% 20%, var(--water-b) 0%, transparent 55%),
      radial-gradient(ellipse at 20% 35%, var(--water-b) 0%, transparent 45%),
      linear-gradient(180deg, var(--water-a) 0%, var(--navy-mid) 60%, var(--navy) 100%);
  }
  .brand {
    position: absolute; top: 70px; left: 0; width: 100%;
    display: flex; justify-content: center; align-items: center; gap: 14px;
  }
  .brand-dot { width: 26px; height: 26px; border-radius: 50%; background: var(--white); }
  .brand-name {
    font-family: "Oswald", sans-serif; font-weight: 600;
    font-size: 40px; letter-spacing: 4px; color: var(--white);
  }
  .cut-line {
    position: absolute; top: 186px; left: 0; width: 100%;
    display: flex; justify-content: center; align-items: center; gap: 16px;
  }
  .cut-line .rule { width: 140px; height: 3px; background: var(--white); }
  .cut-line .cut {
    font-family: "Playfair Display", serif; font-weight: 600;
    font-size: 38px; letter-spacing: 3px; color: var(--white);
  }
  .product-name {
    position: absolute; top: 220px; left: 0; width: 100%; text-align: center;
    font-weight: 800; font-size: 106px; line-height: 1.1; letter-spacing: 1px;
    color: var(--white);
  }
  .product-sub {
    position: absolute; top: 335px; left: 0; width: 100%; text-align: center;
    font-weight: 500; font-size: 22px; letter-spacing: 4px; color: var(--white);
  }
  .window { position: absolute; left: 0; top: 0; }
  .feature-band {
    position: absolute; left: 0; top: 722px; width: 100%; height: 108px;
    background: linear-gradient(90deg, var(--gold-light) 0%, var(--gold-mid) 50%, var(--gold-deep) 100%);
  }
  .feature {
    position: absolute; top: 14px; width: 140px; margin-left: -70px;
    text-align: center; color: var(--white);
  }
  .feature svg { display: block; margin: 0 auto; }
  .feature-title { font-weight: 600; font-size: 18px; line-height: 1.1; margin-top: 8px; }
  .feature-note { font-weight: 500; font-size: 10px; line-height: 1.2; letter-spacing: 0.3px; }
  .net-weight {
    position: absolute; left: 508px; top: 694px; width: 189px; height: 172px;
    background: var(--white); border-radius: 20px 20px 0 0;
    color: var(--ink); text-align: center; padding-top: 34px;
  }
  .net-label { font-weight: 500; font-size: 19px; }
  .net-value { font-weight: 500; font-size: 58px; line-height: 1.1; }
  .net-value sup { font-size: 28px; vertical-align: 24px; margin-left: 2px; }
</style>
</head>
<body>
  <div class="package">
    <div class="water-backdrop" role="img" aria-label="Deep blue rippling sea water texture"></div>

    <div class="brand">
      <span class="brand-dot"></span>
      <span class="brand-name">MAREN</span>
    </div>

    <div class="cut-line">
      <span class="rule"></span><span class="cut">CUT</span><span class="rule"></span>
    </div>
    <div class="product-name">OCTOPUS</div>
    <div class="product-sub">TAKO SASHIMI</div>

    <svg class="window" width="748" height="866" viewBox="0 0 748 866">
      <defs>
        <linearGradient id="productFill" x1="0" y1="0" x2="1" y2="1">
          <stop offset="0" stop-color="var(--product-a)"/>
          <stop offset="0.5" stop-color="var(--product-b)"/>
          <stop offset="1" stop-color="var(--product-a)"/>
        </linearGradient>
      </defs>
      <path role="img" aria-label="Clear window showing cut octopus pieces inside the pack"
            fill="url(#productFill)"
            d="M28,365 C180,335 300,395 430,378 C550,362 630,352 721,372 L721,722 L655,722 C610,700 570,628 470,628 C370,628 320,684 200,672 C120,664 60,660 28,652 Z"/>
    </svg>

    <div class="feature-band">
      <div class="feature" style="left:83px">
        <svg width="40" height="40" viewBox="0 0 40 40"><circle cx="20" cy="20" r="16" fill="var(--white)"/></svg>
        <div class="feature-title">100%</div>
        <div class="feature-note">NATURAL</div>
      </div>
      <div class="feature" style="left:220px">
        <svg width="40" height="40" viewBox="0 0 40 40" stroke="var(--white)" stroke-width="3" stroke-linecap="round" fill="none">
          <line x1="20" y1="3" x2="20" y2="37"/><line x1="5" y1="11.5" x2="35" y2="28.5"/><line x1="5" y1="28.5" x2="35" y2="11.5"/>
          <polyline points="14,6 20,11 26,6"/><polyline points="14,34 20,29 26,34"/>
        </svg>
        <div class="feature-title">FRESHLY</div>
        <div class="feature-note">FROZEN</div>
      </div>
      <div class="feature" style="left:367px">
        <svg width="40" height="40" viewBox="0 0 40 40"><path fill="var(--white)" d="M15,3 H25 V6 H23 V15 L35,35 Q36,38 33,38 H7 Q4,38 5,35 L17,15 V6 H15 Z"/></svg>
        <div class="feature-title">WITHOUT</div>
        <div class="feature-note">PRESERVATIVES</div>
      </div>
    </div>

    <div class="net-weight">
      <div class="net-label">NET WT.</div>
      <div class="net-value">1.0<sup>lb</sup></div>
    </div>
  </div>
</body>
</html>
```